Harborline Energy - needs a business card

Harborline Energy is a U.S. based diesel sourcing and distribution company that supports American oil & gas fields through providing quality product and consistent services.

Target Market(s)

Oil and Gas

Contact Information for Business Card

The background of the card must be white to ensure the logo pops.

Font styles to use
Serif
Sans Serif

Colors

Designer to choose colors to be used in the design.

Requirements
Must have
• Front of Card: Tag line: Harborline Energy, Powering America's Oil & Gas fields.
• Not sure if you guys do this part but just in case...
• Dale Menschow
• Owner/CEO
• C:555.318.4076
• E:Dmenschow@harborlineenergy.example
• W:Harborlineenergy.example
• Locations: Servicing the Powder River, DJ basin and Bakken formations.
• Back of Card: " Frac fueling is what we do. We understand how important diesel fuel is to your operation, which is why our main service line is Frac fueling. We assure our supply and stand by our service"

```html
<!DOCTYPE html>
<html lang="en">
<head>
<meta charset="utf-8">
<title>Harborline Energy – Business Card</title>
<link href="https://fonts.googleapis.com/css2?family=Roboto:wght@400;700&family=Roboto+Condensed:wght@700&family=PT+Sans:wght@400&display=swap" rel="stylesheet">
<style>
  :root {
    --backdrop: #a3a3a3;
    --card: #ffffff;
    --navy: #1e3465;
    --red: #b8202e;
    --ink: #2b2b2b;
    --faint: #eef0f4;
  }
  * { box-sizing: border-box; margin: 0; padding: 0; }
  html, body { width: 1200px; height: 852px; overflow: hidden; }
  body { background: var(--backdrop); position: relative; font-family: "Roboto", sans-serif; }

  .card {
    position: absolute; left: 253px; width: 684px;
    background: var(--card); border-radius: 26px; overflow: hidden;
  }
  .card--front { top: 19px; height: 389px; }
  .card--back { top: 430px; height: 398px; }

  .brand { position: absolute; display: flex; flex-direction: column; align-items: center; }
  .brand__mark { border-radius: 50%; background: var(--navy); }
  .brand__name {
    font-family: "Roboto Condensed", sans-serif; font-weight: 700; color: var(--navy);
    text-transform: uppercase; text-align: center; line-height: 1.05;
  }

  /* front */
  .card--front .brand { left: 39px; top: 28px; width: 210px; }
  .card--front .brand__mark { width: 100px; height: 100px; margin-bottom: 12px; }
  .card--front .brand__name { font-size: 27px; letter-spacing: 1px; }

  .backdrop-circle {
    position: absolute; left: 392px; top: 30px; width: 262px; height: 262px;
    border-radius: 50%; background: var(--faint);
  }

  .person { position: absolute; left: 34px; top: 252px; }
  .person__name { font-family: "Roboto Condensed", sans-serif; font-weight: 700; font-size: 23px; line-height: 28px; color: var(--red); }
  .person__role { font-size: 11px; line-height: 13px; color: var(--ink); }

  .rule { position: absolute; left: 34px; top: 295px; width: 612px; height: 1.5px; background: var(--navy); }

  .contact { position: absolute; left: 32px; top: 300px; list-style: none; }
  .contact__item { display: flex; align-items: center; height: 25px; font-size: 14.5px; color: var(--ink); }
  .contact__icon { width: 24px; height: 20px; margin-right: 11px; }

  .service-area {
    position: absolute; right: 38px; top: 318px; width: 260px;
    text-align: right; font-size: 14px; line-height: 20px; color: var(--ink);
  }

  .band { position: absolute; left: 0; bottom: 0; width: 100%; height: 12px; }

  /* back */
  .card--back .brand { left: 0; width: 100%; top: 48px; }
  .card--back .brand__mark { width: 140px; height: 140px; margin-bottom: 44px; }
  .card--back .brand__name { font-size: 36px; letter-spacing: 1.5px; }
  .statement {
    position: absolute; left: 0; width: 100%; top: 336px;
    text-align: center; font-family: "PT Sans", sans-serif; font-size: 13.5px; line-height: 19px; color: var(--navy);
  }
</style>
</head>
<body>

<section class="card card--front">
  <div class="backdrop-circle"></div>
  <div class="brand">
    <div class="brand__mark"></div>
    <div class="brand__name">Harborline<br>Energy</div>
  </div>

  <div class="person">
    <div class="person__name">Dale Menschow</div>
    <div class="person__role">Owner/CEO</div>
  </div>
  <div class="rule"></div>

  <ul class="contact">
    <li class="contact__item">
      <svg class="contact__icon" viewBox="0 0 22 19"><ellipse cx="11" cy="9.5" rx="10.5" ry="9" fill="#b8202e"/><path d="M7.5 5.5c1-.8 1.8-.4 2.3.6l.5 1.2c.2.6-.3 1-.7 1.3.6 1.3 1.4 2.1 2.6 2.8.4-.4.8-.9 1.4-.6l1.2.6c.9.5 1 1.4.2 2.2-2.6 2.4-9.4-4.3-7.5-8.1z" fill="#fff"/></svg>
      555.318.4076
    </li>
    <li class="contact__item">
      <svg class="contact__icon" viewBox="0 0 22 19"><ellipse cx="11" cy="9.5" rx="10.5" ry="9" fill="#b8202e"/><rect x="6" y="6" width="10" height="7" fill="none" stroke="#fff" stroke-width="1.3"/><path d="M6 6l5 4 5-4" fill="none" stroke="#fff" stroke-width="1.3"/></svg>
      Dmenschow@harborlineenergy.example
    </li>
    <li class="contact__item">
      <svg class="contact__icon" viewBox="0 0 22 19"><ellipse cx="11" cy="9.5" rx="10.5" ry="9" fill="#b8202e"/><circle cx="11" cy="9.5" r="5" fill="none" stroke="#fff" stroke-width="1.2"/><ellipse cx="11" cy="9.5" rx="2" ry="5" fill="none" stroke="#fff" stroke-width="1"/><path d="M6 9.5h10" stroke="#fff" stroke-width="1"/></svg>
      Harborlineenergy.example
    </li>
  </ul>

  <p class="service-area">Servicing the Powder River,DJ basin and<br>Bakken formations</p>

  <svg class="band" viewBox="0 0 684 12" preserveAspectRatio="none">
    <polygon points="0,0 474,0 466,12 0,12" fill="#b8202e"/>
    <polygon points="482,0 684,0 684,12 474,12" fill="#1e3465"/>
  </svg>
</section>

<section class="card card--back">
  <div class="brand">
    <div class="brand__mark"></div>
    <div class="brand__name">Harborline Energy</div>
  </div>
  <p class="statement">
    Frac fueling is what we do.We understand how important diesel fuel is to your operation,<br>
    which is why our main service line is Frac fueling.We assure our supply and stand by our service
  </p>
</section>

</body>
</html>
```